need a clean, modern job advertisement designed for social media (Facebook & Instagram).

The post is to advertise two positions:
• Leading Hand Boilermaker
• Dragline Fitter
We want the design to match our KRT Plant Services branding: blue, white, strong, professional, mining-industry style.
What the design should include:
Bold headline: “WE’RE HIRING”
Sub-headline: “Leading Hand Boilermaker & Dragline Fitter”
Key points:
• Bowen Basin based
• Dragline & shovel maintenance
• Great pay + long-term work
• Locally owned & operated
KRT logo placed cleanly
Space for 1–2 images (boilermaking or dragline work)
Design style:
Strong and industrial
Blue/white colour scheme
Easy to read at a glance
Suitable for a square 1080×1080 design

```html
<!DOCTYPE html>
<html lang="en">
<head>
<meta charset="utf-8">
<title>KRT Plant Services – We Are Hiring</title>
<link href="https://fonts.googleapis.com/css2?family=Oswald:wght@500;600&family=Barlow+Condensed:wght@400;500&family=Poppins:wght@700&display=swap" rel="stylesheet">
<style>
  :root {
    --paper: #2a2a2b;
    --paper-edge: #1f1f20;
    --blue: #0aa2f5;
    --blue-deep: #1479e8;
    --white: #ffffff;
    --silver: #a9abb0;
    --ink: #111111;
    --photo-dark: #1c2350;
    --photo-mid: #3d4fa6;
    --photo-glow: #9fb4ff;
  }
  html, body {
    margin: 0;
    padding: 0;
    width: 1200px;
    height: 1200px;
    overflow: hidden;
    background: var(--paper);
  }
  .post {
    position: relative;
    width: 1200px;
    height: 1200px;
    background: radial-gradient(circle at 30% 30%, #333334, var(--paper) 60%, var(--paper-edge));
    overflow: hidden;
  }
  .curl {
    position: absolute;
    inset: 0;
  }
  .headline {
    margin: 0;
    font-family: "Oswald", sans-serif;
    line-height: 1;
  }
  .headline__top,
  .headline__main {
    position: absolute;
    left: 74px;
    white-space: nowrap;
    transform-origin: left top;
    -webkit-background-clip: text;
    background-clip: text;
    -webkit-text-fill-color: transparent;
  }
  .headline__top {
    top: 126px;
    font-size: 140px;
    font-weight: 500;
    letter-spacing: -2px;
    color: var(--blue);
    background-image: linear-gradient(180deg, var(--blue), var(--blue-deep));
    transform: scaleX(0.89);
  }
  .headline__main {
    top: 256px;
    font-size: 236px;
    font-weight: 600;
    letter-spacing: -3px;
    background-image: linear-gradient(180deg, #ffffff 20%, var(--silver));
    transform: scaleX(0.74);
  }
  .roles {
    position: absolute;
    left: 73px;
    top: 540px;
    height: 100px;
    padding-left: 21px;
    border-left: 9px solid var(--blue);
    font-family: "Poppins", sans-serif;
    font-weight: 700;
    font-size: 44px;
    line-height: 55px;
    color: var(--blue);
    margin: 0;
    box-sizing: border-box;
    white-space: nowrap;
  }
  .roles span { display: block; margin-top: -4px; }
  .perks {
    position: absolute;
    left: 72px;
    top: 690px;
    margin: 0;
    padding: 0;
    list-style: none;
    font-family: "Barlow Condensed", sans-serif;
    font-weight: 400;
    font-size: 42px;
    color: var(--white);
    white-space: nowrap;
    transform: scaleX(0.86);
    transform-origin: left top;
  }
  .perks li {
    display: flex;
    align-items: center;
    height: 53.5px;
  }
  .perks svg { width: 32px; height: 32px; margin-right: 14px; }
  .apply {
    position: absolute;
    left: 73px;
    top: 1027px;
    width: 555px;
    height: 66px;
    display: flex;
    border-radius: 6px;
    overflow: hidden;
    font-family: "Barlow Condensed", sans-serif;
    font-weight: 500;
    white-space: nowrap;
  }
  .apply__label {
    flex: 0 0 199px;
    background: linear-gradient(90deg, var(--blue), var(--blue-deep));
    color: var(--white);
    font-size: 44px;
    letter-spacing: -0.5px;
    display: flex;
    align-items: center;
    justify-content: center;
    border-radius: 6px;
  }
  .apply__email {
    flex: 1;
    background: linear-gradient(90deg, #d9d9d9, #ffffff);
    color: var(--ink);
    font-size: 42px;
    display: flex;
    align-items: center;
    padding-left: 12px;
  }
  .brand {
    position: absolute;
    left: 770px;
    top: 180px;
    display: flex;
    align-items: center;
    gap: 14px;
    font-family: "Oswald", sans-serif;
    font-weight: 600;
    font-size: 40px;
    color: var(--white);
    white-space: nowrap;
  }
  .brand__mark {
    width: 30px;
    height: 30px;
    background: var(--blue);
  }
</style>
</head>
<body>
<main class="post">
  <svg class="curl" viewBox="0 0 1200 1200" width="1200" height="1200">
    <defs>
      <linearGradient id="photoTone" x1="1" y1="0" x2="0" y2="1">
        <stop offset="0" stop-color="#1c2350"/>
        <stop offset="0.55" stop-color="#3d4fa6"/>
        <stop offset="0.8" stop-color="#9fb4ff"/>
        <stop offset="1" stop-color="#1c2350"/>
      </linearGradient>
      <linearGradient id="curlSilver" x1="0" y1="1" x2="1" y2="0">
        <stop offset="0" stop-color="#6e6f73"/>
        <stop offset="0.35" stop-color="#ffffff"/>
        <stop offset="0.7" stop-color="#cfd0d3"/>
        <stop offset="1" stop-color="#4e4f52"/>
      </linearGradient>
    </defs>
    <path role="img" aria-label="Photo of a boilermaker welding steel with sparks flying"
          d="M1200 280 L1200 1200 L640 1200 C720 1195 770 1170 800 1130 Z"
          fill="url(#photoTone)"/>
    <path class="curl__back"
          d="M612 879 C720 800 1010 600 1200 280 L800 1130 C730 1050 670 950 612 879 Z"
          fill="url(#curlSilver)"/>
  </svg>

  <div class="brand">
    <span class="brand__mark"></span>
    <span>KRT Plant Services</span>
  </div>

  <h1 class="headline">
    <span class="headline__top">WE ARE</span>
    <span class="headline__main">HIRING!</span>
  </h1>

  <h2 class="roles">
    <span>LEADING HAND BOILERMAKER</span>
    <span>&amp; DRAGLINE FITTER</span>
  </h2>

  <ul class="perks">
    <li><svg viewBox="0 0 32 32"><path d="M3 17 L12 28 L29 3" fill="none" stroke="#fff" stroke-width="3"/></svg>Bowen Basin based</li>
    <li><svg viewBox="0 0 32 32"><path d="M3 17 L12 28 L29 3" fill="none" stroke="#fff" stroke-width="3"/></svg>Dragline &amp; shovel maintenance</li>
    <li><svg viewBox="0 0 32 32"><path d="M3 17 L12 28 L29 3" fill="none" stroke="#fff" stroke-width="3"/></svg>Great pay + long-term work</li>
    <li><svg viewBox="0 0 32 32"><path d="M3 17 L12 28 L29 3" fill="none" stroke="#fff" stroke-width="3"/></svg>Locally owned &amp; operated</li>
  </ul>

  <div class="apply">
    <span class="apply__label">APPLY NOW!</span>
    <span class="apply__email">jobs@krtplant.com.au</span>
  </div>
</main>
</body>
</html>
```